Postcard About Outsourcing Paperwork

Quillmont, Inc. help nonprofits register so that they can solicit contributions in various states so essentially we are a consulting company who handles paperwork for charities. I have uploaded our logo and a couple other images that we have on our website. We want an oversized post card which on the front says something like "Tired of signing your state registrations". On the back of the card, the right half the card will need name for addresses to print. the right will have spiel about us, but could also have images. The verbiage will be something like "Not only can we file your state registrations, but we can sign and notarize them, and can cut the checks for the state fees. Quillmont file tens of thousands of state registrations each year. Call us today at 555-284-6173 or email us at info@quillmontinc.example to see how we can help you. You can also visit our website at www.quillmontinc.example"

Target Market(s)

We are targeting Charities

Industry/Entity Type

It Company

Requirements
Nice to have
• Our logo(uploaded) and the color blue (matching our logo, website, letterhead) could be good to have

```html
<!DOCTYPE html>
<html lang="en">
<head>
<meta charset="utf-8">
<title>Quillmont, Inc. — State Registration Postcard</title>
<link href="https://fonts.googleapis.com/css2?family=Oswald:wght@600;700&family=Open+Sans:wght@400;600;700;800&display=swap" rel="stylesheet">
<style>
  :root{
    --navy:#0d3f86;
    --blue:#1760b8;
    --sky:#4f9be0;
    --pale:#d7e8f7;
    --ink:#1f2a36;
    --grey:#8a97a6;
    --stamp:#8a9fb5;
    --rule:#b7c0ca;
    --white:#ffffff;
    --page:#ffffff;
  }
  *{box-sizing:border-box;margin:0;padding:0}
  html,body{width:900px;height:1200px;overflow:hidden;background:var(--page)}
  body{font-family:"Open Sans",Arial,sans-serif;color:var(--ink);position:relative}

  .card{position:absolute;left:45px;width:810px;height:570px;background:var(--white);overflow:hidden;box-shadow:0 3px 10px rgba(0,0,0,.25)}
  .card--front{top:30px}
  .card--back{top:615px}

  .swoosh{position:absolute;inset:0;width:100%;height:100%}

  .brand{position:absolute;display:flex;align-items:center;gap:10px}
  .brand__mark{width:30px;height:30px;background:var(--blue)}
  .brand__name{font-weight:700;font-size:24px;color:var(--navy);line-height:1}
  .brand__tag{position:absolute;left:40px;top:32px;font-size:10px;color:var(--grey);white-space:nowrap}
  .card--front .brand{left:170px;top:16px}
  .card--back .brand{left:60px;top:22px}

  .photo{position:absolute}
  .photo--maze-hero{left:0;top:86px;width:430px;height:232px;background:linear-gradient(150deg,#e6eef5 0%,#b9c9d8 55%,#7e97b0 100%)}
  .photo--clock{left:420px;top:348px;width:182px;height:96px;background:radial-gradient(circle at 50% 50%,#f3f3f1 0 28%,#b9bcbf 30% 40%,#6e7d8c 100%)}
  .photo--maze-small{left:608px;top:348px;width:186px;height:96px;background:linear-gradient(135deg,#f1f4f7,#bac7d3)}

  .headline{position:absolute;left:430px;top:118px;width:360px;font-family:"Oswald",Impact,sans-serif;font-weight:700;color:var(--white);font-size:50px;line-height:1.04;text-transform:uppercase;text-align:right}

  .about{position:absolute;left:24px;top:350px;width:370px;font-size:11px;line-height:1.55;color:var(--ink)}

  .contact-band{position:absolute;left:405px;top:452px;width:405px;height:42px;background:var(--pale);display:flex;align-items:center;justify-content:flex-end;padding-right:20px;font-size:18px;color:var(--navy)}
  .contact-band strong{font-weight:700;margin-left:8px}

  .footer{position:absolute;left:0;top:508px;width:810px;height:48px;background:var(--navy);display:flex;align-items:center;justify-content:center;gap:50px;color:var(--white);font-size:16px}
  .footer__item{display:flex;align-items:center;gap:8px}
  .icon{width:18px;height:18px;flex:none}

  .photo--maze-back{left:0;top:102px;width:400px;height:240px;background:linear-gradient(160deg,#eef2f6 0%,#c4d0dc 50%,#8fa5bb 100%)}
  .overlay-text{position:absolute;left:0;top:228px;width:400px;height:114px;background:rgba(23,96,184,.88);color:var(--white);font-size:15px;line-height:1.45;padding:14px 18px}
  .cta{position:absolute;left:28px;top:362px;width:190px;font-weight:800;font-size:19px;line-height:1.25;color:var(--ink)}
  .photo--forms{left:232px;top:372px;width:118px;height:76px;background:linear-gradient(120deg,#f7f8fa,#c9d3de);transform:rotate(-4deg)}
  .back-contacts{position:absolute;left:28px;top:466px;font-size:12px;line-height:1.8;color:var(--ink)}
  .back-contacts div{display:flex;align-items:center;gap:6px}
  .back-contacts .icon{width:12px;height:12px}

  .stamp{position:absolute;left:690px;top:40px;width:80px;height:95px;background:var(--stamp)}
  .address-line{position:absolute;left:520px;width:200px;height:1px;background:var(--rule)}
  .address-line--1{top:290px}
  .address-line--2{top:320px}
  .address-line--3{top:350px}
</style>
</head>
<body>

<section class="card card--front">
  <div class="photo photo--maze-hero" role="img" aria-label="Photo of a person standing in a large white maze"></div>
  <svg class="swoosh" viewBox="0 0 810 570" preserveAspectRatio="none" aria-hidden="true">
    <path d="M430 84 C560 80 700 72 810 62 V330 H400 C440 260 452 160 430 84 Z" fill="var(--blue)"/>
    <path d="M412 84 C442 160 432 262 386 330 L402 330 C452 262 458 160 432 84 Z" fill="var(--navy)"/>
    <path d="M0 78 C220 74 520 70 810 54 V64 C520 80 220 84 0 88 Z" fill="var(--navy)"/>
    <path d="M0 314 C150 324 300 324 396 318 L392 328 C300 336 150 336 0 326 Z" fill="var(--sky)"/>
  </svg>

  <div class="brand">
    <span class="brand__mark"></span>
    <span class="brand__name">Quillmont, Inc.</span>
    <span class="brand__tag">The state registration professionals</span>
  </div>

  <h1 class="headline">Tired of filing<br>your state<br>registrations?</h1>

  <p class="about">Quillmont, Inc. has been specializing in state registrations since the 1980's and we file tens of thousands of state registrations each year. Charitable state registration is not a sideline at Quillmont – it's all we do. We handle every aspect of the registration process including signing the forms and writing the checks. We would love to talk to you about helping you get registered.</p>

  <div class="photo photo--clock" role="img" aria-label="Photo of a wall clock"></div>
  <div class="photo photo--maze-small" role="img" aria-label="Photo of a white maze seen from above"></div>

  <div class="contact-band">contact us <strong>555-284-6173</strong></div>

  <footer class="footer">
    <span class="footer__item">
      <svg class="icon" viewBox="0 0 18 18"><rect x="1" y="4" width="16" height="11" fill="#fff"/><path d="M1 4 L9 10 L17 4" stroke="var(--navy)" stroke-width="1.5" fill="none"/></svg>
      info@quillmontinc.example
    </span>
    <span class="footer__item">
      <svg class="icon" viewBox="0 0 18 18"><circle cx="9" cy="9" r="7.5" fill="none" stroke="#fff" stroke-width="1.5"/><path d="M1.5 9 H16.5 M9 1.5 C5 5 5 13 9 16.5 C13 13 13 5 9 1.5" stroke="#fff" stroke-width="1.2" fill="none"/></svg>
      www.quillmontinc.example
    </span>
  </footer>
</section>

<section class="card card--back">
  <svg class="swoosh" viewBox="0 0 810 570" preserveAspectRatio="none" aria-hidden="true">
    <path d="M0 90 C150 84 300 86 420 92 V100 H0 Z" fill="var(--blue)"/>
    <path d="M0 528 C70 548 130 560 200 570 H0 Z" fill="var(--blue)"/>
    <path d="M0 548 C50 558 90 565 130 570 H0 Z" fill="var(--navy)"/>
  </svg>

  <div class="brand">
    <span class="brand__mark"></span>
    <span class="brand__name">Quillmont, Inc.</span>
    <span class="brand__tag">The state registration professionals</span>
  </div>

  <div class="photo photo--maze-back" role="img" aria-label="Photo of a white maze with walls in perspective"></div>
  <p class="overlay-text">Not only can we file your state registrations, but we can sign and notarize them, and can cut the checks for the state fees.</p>

  <p class="cta">Contact us today to find out how we can help you!</p>
  <div class="photo photo--forms" role="img" aria-label="Photo of registration forms and a pen"></div>

  <div class="back-contacts">
    <div><svg class="icon" viewBox="0 0 14 14"><path d="M3 1 L5.5 1 L6.5 4 L5 5.5 C6 7.5 6.5 8 8.5 9 L10 7.5 L13 8.5 V11 C13 12 12 13 11 13 C5.5 13 1 8.5 1 3 C1 2 2 1 3 1Z" fill="var(--blue)"/></svg>555-284-6173</div>
    <div><svg class="icon" viewBox="0 0 14 14"><rect x="1" y="3" width="12" height="8" fill="var(--blue)"/><path d="M1 3 L7 8 L13 3" stroke="#fff" fill="none"/></svg>info@quillmontinc.example</div>
  </div>

  <div class="stamp"></div>
  <div class="address-line address-line--1"></div>
  <div class="address-line address-line--2"></div>
  <div class="address-line address-line--3"></div>
</section>

</body>
</html>
```